real esate business card with company logo and name

we need a business card design for a real esate company

The company name is Walsh & Ortiz Pty Ltd, and we have our logo designed and will upload. We want classic or moden feel. Black or white background. looks more textured. Should include folowinginformations
Paul Walsh and Tara Ortiz
Sales Agents & Onsite Manager
p: 07 5948 2610
F: 07 5948 2795
M:0451 786 923
3/22 Marlow Crescent, ELLEN GROVE QLD 4078

We want this business card looks professonal. Thank you in advance.

Industry/Entity Type

Real Estate Agent

Contact Information for Business Card

Paul Walsh and Tara Ortiz
Onsite Manager & Sales Agents
p: 07 5948 2610
M:0451 786 923

Font styles to use
Serif

Colors
000000
fbfbfb
333333
959595

Requirements
Must have
• company logo and name, black or white back ground

```html
<!DOCTYPE html>
<html lang="en">
<head>
<meta charset="utf-8">
<title>Walsh &amp; Ortiz Pty Ltd — Business Card</title>
<link href="https://fonts.googleapis.com/css2?family=Lato:wght@400;700&family=Oswald:wght@300&display=swap" rel="stylesheet">
<style>
  :root {
    --stage: #333333;
    --card: #000000;
    --ink: #fbfbfb;
    --ink-soft: #d9d9d9;
    --muted: #959595;
    --rule: #4a4a4a;
  }
  * { box-sizing: border-box; margin: 0; padding: 0; }
  html, body {
    width: 1200px; height: 1086px; overflow: hidden;
    background: var(--stage);
    font-family: "Lato", sans-serif;
  }
  .card {
    position: absolute;
    left: 254px;
    width: 678px;
    height: 386px;
    background: var(--card);
    box-shadow: 0 6px 18px rgba(0,0,0,0.45);
  }
  .card--front { top: 126px; }
  .card--back { top: 586px; }

  .brand {
    position: absolute;
    display: flex; flex-direction: column; align-items: center;
  }
  .brand__square { background: var(--muted); }
  .brand__name {
    color: var(--muted);
    font-family: "Oswald", sans-serif;
    font-weight: 300;
    text-transform: uppercase;
    letter-spacing: 0.02em;
    line-height: 1.2;
    white-space: nowrap;
  }
  .card--front .brand { left: 46px; width: 300px; top: 90px; }
  .card--front .brand__square { width: 172px; height: 172px; margin-bottom: 20px; }
  .card--front .brand__name { font-size: 23px; }

  .card--back .brand { left: 0; width: 100%; top: 54px; }
  .card--back .brand__square { width: 218px; height: 218px; margin-bottom: 26px; }
  .card--back .brand__name { font-size: 30px; }

  .divider {
    position: absolute; left: 340px; top: 90px;
    width: 1px; height: 218px; background: var(--rule);
  }
  .contact { position: absolute; left: 364px; top: 84px; color: var(--ink); }
  .contact__name { font-size: 27px; font-weight: 700; line-height: 1.1; }
  .contact__role { font-size: 18px; color: var(--ink-soft); margin-top: 2px; }
  .contact__lines { list-style: none; margin-top: 28px; }
  .contact__lines li {
    display: flex; align-items: center; gap: 6px;
    font-size: 21px; line-height: 26px;
  }
  .contact__lines svg { width: 16px; height: 16px; fill: var(--ink); flex: none; }
  .contact__address { font-size: 18px; line-height: 24px; margin-top: 14px; color: var(--ink-soft); }
</style>
</head>
<body>
  <section class="card card--front">
    <div class="brand">
      <div class="brand__square"></div>
      <div class="brand__name">Walsh &amp; Ortiz Pty Ltd.</div>
    </div>
    <div class="divider"></div>
    <div class="contact">
      <h1 class="contact__name">Paul Walsh</h1>
      <p class="contact__role">Sales Agents</p>
      <ul class="contact__lines">
        <li><svg viewBox="0 0 16 16" aria-hidden="true"><path d="M4 1h8a1 1 0 0 1 1 1v12a1 1 0 0 1-1 1H4a1 1 0 0 1-1-1V2a1 1 0 0 1 1-1zm1 2v9h6V3zm3 10a.8.8 0 1 0 0 .01z"/></svg>0451 786 923</li>
        <li><svg viewBox="0 0 16 16" aria-hidden="true"><path d="M1 6c0-2 3-3 7-3s7 1 7 3v1h-4V5.5H5V7H1zm3 2h8l2 6H2z"/></svg>07 5948 2610</li>
        <li><svg viewBox="0 0 16 16" aria-hidden="true"><path d="M4 1h8v4H4zM1 6h14v6h-3v3H4v-3H1zm4 4v3h6v-3z"/></svg>07 5948 2795</li>
      </ul>
      <p class="contact__address">3/22 Marlow Crescent<br>BRAYFIELD VIC 3942</p>
    </div>
  </section>

  <section class="card card--back">
    <div class="brand">
      <div class="brand__square"></div>
      <div class="brand__name">Walsh &amp; Ortiz Pty Ltd.</div>
    </div>
  </section>
</body>
</html>
```